Redesign Login page

I want to redesign my login page to bring my 2 products closer together. I am only looking to redesign one login page, not 2.

For the logo, please make it solid and it can be black or white if helpful. I can also fine tune the logo if you get it close.

Coding

Coded - Design and coding required

Number of Pages Required

1 page

```html
<!DOCTYPE html>
<html lang="en">
<head>
<meta charset="utf-8">
<title>Trailmark – Login</title>
<link href="https://fonts.googleapis.com/css2?family=Poppins:wght@400;500;600;700&display=swap" rel="stylesheet">
<style>
  :root {
    --bg-center: #2b4b49;
    --bg-mid: #16302e;
    --bg-edge: #081614;
    --card: #ffffff;
    --logo-panel: #ebebeb;
    --ink: #0d2e2a;
    --ink-soft: #4b6a66;
    --field-border: #bdbdbd;
    --field-text: #3a3a3a;
    --icon: #333333;
    --button: #0a2c28;
    --button-text: #ffffff;
    --brand: #111111;
  }
  * { box-sizing: border-box; margin: 0; padding: 0; }
  html, body { width: 1200px; height: 738px; overflow: hidden; }
  body { font-family: "Poppins", sans-serif; position: relative; }
  .backdrop {
    position: absolute; inset: 0;
    background: radial-gradient(ellipse 60% 65% at 50% 30%, var(--bg-center) 0%, var(--bg-mid) 55%, var(--bg-edge) 100%);
  }
  .login-card {
    position: absolute; left: 388px; top: 114px; width: 424px; height: 509px;
    background: var(--card); border-radius: 11px;
    box-shadow: 0 8px 18px rgba(0,0,0,0.35);
  }
  .brand-panel {
    position: absolute; left: 15px; top: 17px; width: 390px; height: 110px;
    background: var(--logo-panel); border-radius: 11px;
    display: flex; align-items: center; justify-content: center;
  }
  .brand-name { font-size: 44px; font-weight: 700; color: var(--brand); letter-spacing: -1px; }
  .field-label {
    position: absolute; left: 14px; font-size: 16px; font-weight: 700; color: var(--ink);
  }
  .field {
    position: absolute; left: 15px; width: 390px; height: 51px;
    border: 1px solid var(--field-border); border-radius: 6px;
    display: flex; align-items: center; justify-content: space-between;
    padding: 0 16px 0 15px; font-size: 13.6px; color: var(--field-text);
  }
  .field svg { width: 14px; height: 14px; fill: var(--icon); }
  .alt-user {
    position: absolute; left: 14px; top: 342px;
    font-size: 12.8px; font-weight: 600; color: var(--ink-soft);
  }
  .remember {
    position: absolute; left: 14px; top: 463px;
    display: flex; align-items: center; gap: 7px; font-size: 13px; color: var(--ink);
  }
  .remember svg { width: 11px; height: 11px; }
  .login-button {
    position: absolute; left: 15px; top: 380px; width: 390px; height: 52px;
    background: var(--button); border-radius: 6px;
    display: flex; align-items: center; justify-content: center;
    color: var(--button-text); font-size: 15px; font-weight: 700;
  }
  .help-line {
    position: absolute; left: 0; width: 100%; text-align: center;
    font-size: 13px; color: var(--ink-soft);
  }
  .help-line strong { color: var(--ink); font-weight: 700; }
</style>
</head>
<body>
  <div class="backdrop" role="img" aria-label="Dark teal background with faint topographic contour lines"></div>

  <main class="login-card">
    <div class="brand-panel"><span class="brand-name">Trailmark</span></div>

    <div class="field-label" style="top:141px;">User ID</div>
    <div class="field" style="top:169px;">
      <span>Username</span>
      <svg viewBox="0 0 16 16" aria-hidden="true"><circle cx="8" cy="4.5" r="3.5"/><path d="M1 16c0-4 3-6.5 7-6.5s7 2.5 7 6.5z"/></svg>
    </div>
    <div class="alt-user" style="top:229px;">Login with a different user ID</div>

    <div class="field-label" style="top:260px;">Password</div>
    <div class="field" style="top:290px;">
      <span>***********</span>
      <svg viewBox="0 0 16 16" aria-hidden="true"><circle cx="10.5" cy="5.5" r="4.5"/><path d="M7 8l-6 6v2h3v-2h2v-2h2l1.5-1.5z"/></svg>
    </div>

    <div class="remember" style="top:351px;">
      <svg viewBox="0 0 12 12" aria-hidden="true"><rect x="0.75" y="0.75" width="10.5" height="10.5" rx="1.5" fill="none" stroke="#0d2e2a" stroke-width="1.3"/><path d="M3 6.2l2 2 4-4.2" fill="none" stroke="#0d2e2a" stroke-width="1.4"/></svg>
      <span>Save user ID</span>
    </div>

    <div class="login-button">Login</div>

    <div class="help-line" style="top:446px;">Forgot user ID ? &nbsp;|&nbsp; Forgot Password?</div>
    <div class="help-line" style="top:469px;">Don’t have an account? &nbsp;| <strong>Sign Up</strong></div>
  </main>
</body>
</html>
```